The Birchfall Reel----- Wade Pellinger----- Umpqua River Smallmouth ------www.thebirchfallreel-demo.com-----

Hello Fishermen,
The Umpqua rivers peaceful beauty is like no other river, the private Loop section offers trophy bass fishing along with 100 fish days. Spin cast or fly fish for bass. This 8 hour fishing trip takes you into a remote section of ranches and wilderness abundant with not only thousands of bass per mile...... but wildlife and scenery are breath taking in this quite section of river.
This trip is for everyone, easy for the Grand Parents and the grand kids...... Women love this trip with the warm weather and easy fishing.
So Let's go Fishing...... please call or email us today and book your trip or with any questions you have.
Vacation Rentals, Motels and R.V parks all available close by.

Email us at: birchfallreel@mailvale-demo.net
Visit our website at: www.thebirchfallreel-demo.com
Call us at: 541-555-0148

Thank you for fishing with us,
Wade Pellinger

return address;
Wade Pellinger
p.o. box 712
Elkton, Oregon 97781

****NOTE for front of post card layout person should go to our website home page for ideas, and photos. Please feel free to change our message above to correct grammar and make read smoother, Thank you.....

there is no contest....not sure how that got there...

```html
<!DOCTYPE html>
<html lang="en">
<head>
<meta charset="utf-8">
<title>Wade Pellinger Fishing Guide &amp; Outfitter – Postcard</title>
<link rel="stylesheet" href="https://fonts.googleapis.com/css2?family=Didact+Gothic&family=Open+Sans:wght@600;700&display=swap">
<style>
  :root{
    --backdrop:#2b2b2b;
    --paper:#ffffff;
    --river-blue:#0f4e70;
    --deep-blue:#0d4663;
    --guide-green:#1f8a5b;
    --ink:#1c2a33;
    --logo-teal:#1a5a72;
    --alert-red:#e0262b;
    --label-grey:#e6e7e8;
    --olive:#7d7a2e;
    --photo-a:#5d8a5a;
    --photo-b:#6f8fa3;
  }
  *{box-sizing:border-box;margin:0;padding:0}
  html,body{width:900px;height:1200px;overflow:hidden}
  body{background:var(--backdrop);position:relative;font-family:"Didact Gothic",sans-serif;color:var(--ink)}
  .card{position:absolute;left:128px;width:647px;height:495px;background:var(--paper);overflow:hidden}
  .card--front{top:73px}
  .card--back{top:617px}
  .art{position:absolute;left:0;top:0}

  /* front */
  .brand{position:absolute;left:38px;top:20px;display:flex;align-items:center;gap:10px}
  .brand__mark{width:26px;height:26px;border-radius:50%;background:var(--guide-green)}
  .brand__name{font-family:"Didact Gothic",sans-serif;color:var(--logo-teal);font-size:19px;line-height:21px}
  .call-box{position:absolute;left:387px;top:12px;width:260px;height:63px;padding:6px 0 0 7px;
    background:linear-gradient(90deg,#ffffff 0%,#e9eff3 45%,#a8c0cd 100%);font-size:13px;line-height:15px;color:var(--ink)}
  .call-box strong{font-family:"Open Sans",sans-serif;font-weight:700}
  .call-box__phone{display:block;font-size:22px;line-height:28px;color:var(--deep-blue)}
  .offer-title{position:absolute;left:274px;top:109px;width:335px;height:28px;background:var(--deep-blue);
    color:#fff;font-family:"Didact Gothic",sans-serif;font-weight:400;font-size:21px;line-height:28px;padding-left:15px;border-radius:2px}
  .offer-list{position:absolute;left:276px;top:146px;list-style:none;font-size:15.5px;line-height:28px;color:var(--ink)}
  .offer-list li::before{content:"";display:inline-block;width:6px;height:6px;border-radius:50%;background:var(--deep-blue);margin:0 9px 2px 0;vertical-align:middle}
  .tagline{position:absolute;left:31px;top:393px;width:300px;color:#fff;font-size:19px;line-height:24px}
  .front-url{position:absolute;right:10px;top:468px;color:#fff;font-size:14.5px}

  /* back */
  .nearby{position:absolute;left:0;top:13px;width:375px;height:43px;background:var(--label-grey);
    color:var(--alert-red);font-family:"Open Sans",sans-serif;font-weight:700;font-size:13.5px;line-height:17px;text-align:center;padding-top:4px}
  .section-tag{position:absolute;left:22px;width:151px;height:22px;background:#fff;border-radius:0 8px 0 0;
    font-family:"Open Sans",sans-serif;font-weight:700;font-size:17px;line-height:22px;color:var(--ink);padding-left:5px;box-shadow:2px 2px 0 rgba(0,0,0,.25)}
  .section-tag--about{top:77px}
  .section-tag--contact{top:307px}
  .about-text{position:absolute;left:25px;top:108px;width:293px;color:#fff;font-size:16.5px;line-height:18.3px;text-align:justify}
  .contact-list{position:absolute;left:22px;top:340px;list-style:none;color:#fff;font-size:16.5px;line-height:18.5px}
  .contact-list li{display:flex;gap:7px;align-items:flex-start}
  .contact-list .gap{margin-top:11px}
  .contact-list svg{flex:none;margin-top:3px}
  .stamp-box{position:absolute;left:556px;top:19px;width:60px;height:59px;border:1px solid #333}
  .address-line{position:absolute;left:372px;width:242px;height:1px;background:#555}
</style>
</head>
<body>

<section class="card card--front" aria-label="Postcard front">
  <svg class="art" width="647" height="495" viewBox="0 0 647 495" aria-hidden="true">
    <path d="M0,86 C120,210 300,365 647,392 L647,495 L0,495 Z" fill="var(--guide-green)"/>
    <path d="M0,150 C150,270 320,385 647,408 L647,495 L0,495 Z" fill="var(--river-blue)"/>
  </svg>

  <div class="brand">
    <span class="brand__mark"></span>
    <span class="brand__name">Wade Pellinger<br>Fishing Guide &amp; Outfitter</span>
  </div>

  <div class="call-box">Please <strong>Call Us</strong> today for<br>any question and book your trip:
    <span class="call-box__phone">541-555-0148</span></div>

  <h2 class="offer-title">UMPQUA RIVER SMALLMOUTH</h2>
  <ul class="offer-list">
    <li>Spin cast or fly fish for bass.</li>
    <li>Thousands of bass per mile, 100 fish days.</li>
    <li>This is an 8 hour trip On the UMPQUA River.</li>
  </ul>

  <svg class="art" width="647" height="495" viewBox="0 0 647 495">
    <defs>
      <linearGradient id="photoTone" x1="0" y1="0" x2="0" y2="1">
        <stop offset="0" stop-color="var(--photo-b)"/>
        <stop offset="1" stop-color="var(--photo-a)"/>
      </linearGradient>
    </defs>
    <circle cx="104" cy="232" r="77" fill="url(#photoTone)" stroke="var(--guide-green)" stroke-width="6" role="img" aria-label="Photo: angler holding catch beside a drift boat"/>
    <circle cx="252" cy="310" r="67" fill="url(#photoTone)" stroke="var(--guide-green)" stroke-width="6" role="img" aria-label="Photo: two anglers showing their fish on the river"/>
    <circle cx="379" cy="368" r="53" fill="url(#photoTone)" stroke="var(--guide-green)" stroke-width="6" role="img" aria-label="Photo: young angler on a dock with two fish"/>
    <circle cx="524" cy="397" r="55" fill="url(#photoTone)" stroke="var(--guide-green)" stroke-width="6" role="img" aria-label="Photo: angler holding a bass by the water"/>
  </svg>

  <p class="tagline">This trip is for everyone, easy for the Grand Parents and the grand kids......</p>
  <p class="front-url">www.thebirchfallreel-demo.com</p>
</section>

<section class="card card--back" aria-label="Postcard back">
  <svg class="art" width="647" height="495" viewBox="0 0 647 495" aria-hidden="true">
    <polygon points="0,0 370,0 302,495 0,495" fill="var(--river-blue)"/>
    <polygon points="362,56 375,56 375,44" fill="var(--olive)"/>
  </svg>

  <p class="nearby">Vacation Rentals, Motels and R.V parks<br>all available close by.</p>

  <h3 class="section-tag section-tag--about">About River:</h3>
  <p class="about-text">The Umpqua rivers peaceful beauty is like no other river, the private Loop section offers trophy bass fishing along with 100 fish days. Spin cast or fly fish for bass. This 8 hour fishing trip takes you into a remote section of ranches and wilderness abundant with not only thousands of bass per mile...... but wildlife and scenery are breath taking in this quite section of river.</p>

  <h3 class="section-tag section-tag--contact">Contact us:</h3>
  <ul class="contact-list">
    <li><svg width="10" height="13" viewBox="0 0 10 13"><path d="M5 0a5 5 0 0 0-5 5c0 3.5 5 8 5 8s5-4.5 5-8a5 5 0 0 0-5-5zm0 7a2 2 0 1 1 0-4 2 2 0 0 1 0 4z" fill="#fff"/></svg>
      <span>Wade Pellinger<br>&nbsp;p.o. box 712<br>Elkton, Oregon 97781</span></li>
    <li class="gap"><svg width="12" height="12" viewBox="0 0 12 12"><path d="M2.5 0.5l2 2.5-1.2 1.5c.8 1.7 2.1 3 3.8 3.8L8.6 7l2.6 2-1 2.4C5 11 1 7 .6 1.6z" fill="#fff"/></svg><span>541-555-0148</span></li>
    <li><svg width="12" height="12" viewBox="0 0 12 12"><circle cx="6" cy="6" r="5.3" fill="none" stroke="#fff" stroke-width="1.2"/><path d="M.7 6h10.6M6 .7c-3 3-3 7.6 0 10.6M6 .7c3 3 3 7.6 0 10.6" fill="none" stroke="#fff" stroke-width="1"/></svg><span>www.thebirchfallreel-demo.com</span></li>
    <li><svg width="13" height="10" viewBox="0 0 13 10"><rect x=".5" y=".5" width="12" height="9" fill="none" stroke="#fff"/><path d="M.5 .5l6 5 6-5" fill="none" stroke="#fff"/></svg><span>birchfallreel@mailvale-demo.net</span></li>
  </ul>

  <div class="stamp-box" aria-label="Stamp area"></div>
  <div class="address-line" style="top:273px"></div>
  <div class="address-line" style="top:318px"></div>
  <div class="address-line" style="top:361px"></div>
</section>

</body>
</html>
```